Creative Stationary For Security Solutions Company
Halvern Guard Services
Creative Stationary For Security Solutions Company - Security
Creative Brief
Professional
Wesley Kolvasky
wesley@halvernguard.example
www.halvernguard.example
California PI No. 51928 And California PPO No. 40261
Logo has been uploaded in different color variations. Feel free to experiment, however I prefer the logo with black highlights on the visor, nose and neck (#1 I believe) I will provide my phone numbers towards the end of the project. Thanks and have fun.
I would like to see my logo on one side and info on the other. But feel free to experiment.

```html
<!DOCTYPE html>
<html lang="en">
<head>
<meta charset="utf-8">
<title>Halvern Guard Services – Business Card</title>
<link rel="stylesheet" href="https://fonts.googleapis.com/css2?family=Montserrat:wght@400;500;600;700&display=swap">
<style>
  :root{
    --stage:#e7e7e9;
    --card-light:#ffffff;
    --card-dark:#0b0b0c;
    --ink:#262a2e;
    --ink-soft:#5b5f63;
    --accent:#e2672a;
    --rule:#3a3d40;
    --on-dark:#f4f4f4;
  }
  *{box-sizing:border-box;margin:0;padding:0}
  html,body{width:1200px;height:901px;overflow:hidden}
  body{
    background:var(--stage);
    font-family:"Montserrat",sans-serif;
    display:flex;flex-direction:column;align-items:center;justify-content:center;gap:36px;
  }
  .card{
    width:700px;height:400px;border-radius:22px;position:relative;
    box-shadow:0 10px 30px rgba(0,0,0,.18);
    overflow:hidden;
  }
  /* back */
  .card--back{background:var(--card-dark);display:flex;align-items:center;justify-content:center}
  .brand{display:flex;align-items:center;gap:18px}
  .brand__dot{width:64px;height:64px;border-radius:50%;background:var(--accent);flex:none}
  .brand__name{font-weight:700;font-size:30px;letter-spacing:.04em;text-transform:uppercase;color:var(--on-dark);line-height:1.15}
  /* front */
  .card--front{background:var(--card-light);display:flex;align-items:center}
  .front__identity{width:330px;display:flex;justify-content:center}
  .front__identity .brand{flex-direction:column;gap:14px;align-items:center;text-align:center}
  .front__identity .brand__dot{width:72px;height:72px}
  .front__identity .brand__name{color:var(--ink);font-size:22px}
  .front__rule{width:2px;height:150px;background:var(--rule);margin-right:44px}
  .front__details{flex:1}
  .person__name{color:var(--accent);font-weight:600;font-size:20px}
  .person__role{color:var(--ink-soft);font-size:12px;margin-top:4px}
  .contacts{list-style:none;margin-top:46px;display:grid;grid-template-columns:18px auto;column-gap:12px;row-gap:4px;align-items:center;font-size:12.5px;color:var(--ink)}
  .contacts svg{width:14px;height:14px;fill:var(--accent)}
</style>
</head>
<body>
  <section class="card card--back" aria-label="Card back">
    <div class="brand">
      <span class="brand__dot"></span>
      <span class="brand__name">Halvern Guard<br>Services</span>
    </div>
  </section>

  <section class="card card--front" aria-label="Card front">
    <div class="front__identity">
      <div class="brand">
        <span class="brand__dot"></span>
        <span class="brand__name">Halvern Guard<br>Services</span>
      </div>
    </div>
    <div class="front__rule"></div>
    <div class="front__details">
      <p class="person__name">Wesley Kolvasky</p>
      <p class="person__role">Founder</p>
      <ul class="contacts">
        <svg viewBox="0 0 16 16" aria-hidden="true"><path d="M3 2h3l1 3-2 1.5a9 9 0 0 0 4.5 4.5L11 9l3 1v3a1 1 0 0 1-1 1A11 11 0 0 1 2 3a1 1 0 0 1 1-1z"/></svg>
        <li>999-999-9999</li>
        <svg viewBox="0 0 16 16" aria-hidden="true"><path d="M5 1h6a1 1 0 0 1 1 1v12a1 1 0 0 1-1 1H5a1 1 0 0 1-1-1V2a1 1 0 0 1 1-1zm0 2v9h6V3z"/></svg>
        <li>999-999-9999</li>
        <svg viewBox="0 0 16 16" aria-hidden="true"><path d="M4 1h8v4H4zM2 6h12a1 1 0 0 1 1 1v5h-3v3H4v-3H1V7a1 1 0 0 1 1-1zm3 5v3h6v-3z"/></svg>
        <li>999-999-9999</li>
        <svg viewBox="0 0 16 16" aria-hidden="true"><path d="M1 3h14v10H1zm1.5 1.5L8 9l5.5-4.5V4h-11z"/></svg>
        <li>wesley@halvernguard.example</li>
        <svg viewBox="0 0 16 16" aria-hidden="true"><path d="M8 1a7 7 0 1 0 0 14A7 7 0 0 0 8 1zm0 1.6c.9 1.2 1.5 2.9 1.6 4.6H6.4C6.5 5.5 7.1 3.8 8 2.6zM6.4 8.8h3.2c-.1 1.7-.7 3.4-1.6 4.6-.9-1.2-1.5-2.9-1.6-4.6zM2.7 7.2a5.4 5.4 0 0 1 2.6-3.8 9 9 0 0 0-1 3.8zm0 1.6h1.6a9 9 0 0 0 1 3.8 5.4 5.4 0 0 1-2.6-3.8zm8.1 3.8a9 9 0 0 0 1-3.8h1.6a5.4 5.4 0 0 1-2.6 3.8zm1-5.4a9 9 0 0 0-1-3.8 5.4 5.4 0 0 1 2.6 3.8z"/></svg>
        <li>www.halvernguard.example</li>
      </ul>
    </div>
  </section>
</body>
</html>
```